Banner for County Fair

Need a banner with our logo primarily, but some other color/background work. Also include city name Brenhollow, NE. Tagline that could be used is Fiber Optic Fast! Also visit www.tolbrinkdata.com to get a feel for the company.

```html
<!DOCTYPE html>
<html lang="en">
<head>
<meta charset="utf-8">
<title>Tolbrink County Fair Banner</title>
<link rel="stylesheet" href="https://fonts.googleapis.com/css2?family=Montserrat:wght@700;800&family=Raleway:wght@400;500&display=swap">
<style>
  :root {
    --brand-blue: #2a73a0;
    --deep-blue: #1f5f88;
    --sky-blue: #3f9fc9;
    --silver: #d9dde0;
    --white: #ffffff;
    --page: #eef1f3;
  }
  html, body {
    margin: 0;
    width: 1086px;
    height: 1200px;
    overflow: hidden;
    background: var(--page);
  }
  .banner {
    position: absolute;
    left: 43px;
    top: 439px;
    width: 1000px;
    height: 322px;
    overflow: hidden;
    background: var(--brand-blue);
    box-shadow: 0 6px 18px rgba(0,0,0,0.18);
  }
  .banner-art {
    position: absolute;
    inset: 0;
  }
  .brand {
    position: absolute;
    left: 575px;
    top: 30px;
    display: flex;
    align-items: center;
    gap: 10px;
    font-family: "Montserrat", sans-serif;
    font-weight: 800;
    font-size: 42px;
    line-height: 1;
    letter-spacing: -1px;
    color: var(--brand-blue);
  }
  .brand-dot {
    width: 16px;
    height: 16px;
    border-radius: 50%;
    background: var(--brand-blue);
  }
  .tagline {
    position: absolute;
    left: 640px;
    top: 120px;
    width: 360px;
    height: 56px;
    box-sizing: border-box;
    padding-right: 14px;
    background: var(--white);
    display: flex;
    align-items: center;
    justify-content: flex-end;
    font-family: "Montserrat", sans-serif;
    font-weight: 700;
    font-size: 29px;
    color: var(--deep-blue);
  }
  .location {
    position: absolute;
    left: 688px;
    top: 222px;
    width: 288px;
    height: 48px;
    box-sizing: border-box;
    border: 1.5px solid var(--white);
    display: flex;
    align-items: center;
    justify-content: center;
    padding-top: 4px;
    font-family: "Raleway", sans-serif;
    font-weight: 500;
    font-size: 32px;
    line-height: 1;
    color: var(--white);
    white-space: nowrap;
  }
  .location-pin {
    position: absolute;
    left: 820px;
    top: 202px;
    width: 22px;
    height: 28px;
  }
  .website {
    position: absolute;
    left: 700px;
    top: 282px;
    display: flex;
    align-items: center;
    gap: 7px;
    font-family: "Raleway", sans-serif;
    font-size: 17px;
    line-height: 1.2;
    color: var(--white);
    white-space: nowrap;
  }
  .website-icon {
    width: 11px;
    height: 11px;
    border-radius: 50%;
    border: 2px solid var(--white);
    box-sizing: border-box;
  }
</style>
</head>
<body>
  <section class="banner">
    <svg class="banner-art" width="1000" height="322" viewBox="0 0 1000 322">
      <defs>
        <linearGradient id="photoTone" x1="0" y1="0" x2="1" y2="0">
          <stop offset="0" stop-color="#e9edf1"/>
          <stop offset="0.25" stop-color="#d8b9a3"/>
          <stop offset="0.55" stop-color="#e8cbdc"/>
          <stop offset="0.8" stop-color="#a9cbe3"/>
          <stop offset="1" stop-color="#ffffff"/>
        </linearGradient>
        <clipPath id="openArea">
          <path d="M108,0 H908 L820,172 C760,250 640,285 520,285 C330,285 160,190 108,0 Z"/>
        </clipPath>
      </defs>
      <path class="swoosh-silver" d="M92,0 C120,190 290,322 470,322 H360 C220,290 110,170 92,0 Z" fill="var(--silver)"/>
      <path class="swoosh-blue" d="M104,0 C150,200 330,300 520,298 C640,297 740,262 800,215 C730,282 620,322 500,322 H470 C290,322 120,190 104,0 Z" fill="var(--sky-blue)"/>
      <path class="open-area" d="M108,0 H908 L820,172 C760,250 640,285 520,285 C330,285 160,190 108,0 Z" fill="var(--white)"/>
      <g clip-path="url(#openArea)">
        <rect class="family-photo" role="img" aria-label="Photo of a smiling family of four gathered around a laptop at home" x="108" y="0" width="640" height="290" fill="url(#photoTone)"/>
      </g>
      <path class="tagline-shadow" d="M660,176 H1000 V186 H650 Z" fill="#b8c2c9" opacity="0.7"/>
    </svg>

    <div class="brand"><span class="brand-dot"></span>TOLBRINK</div>

    <div class="tagline">FIBER OPTIC FAST!</div>

    <svg class="location-pin" viewBox="0 0 24 30" aria-hidden="true">
      <path d="M12,1 C6,1 2,5.5 2,11 C2,18 12,29 12,29 C12,29 22,18 22,11 C22,5.5 18,1 12,1 Z" fill="var(--white)"/>
      <circle cx="12" cy="11" r="4" fill="var(--brand-blue)"/>
    </svg>
    <div class="location">Brenhollow, NE</div>

    <div class="website"><span class="website-icon"></span>www.tolbrinkdata.com</div>
  </section>
</body>
</html>
```